"Lantern Over Fields" Gospel Presentation Booklet

I need a design for a 12 page (including front/back cover) square booklet, with religious images and aesthetically pleasing fonts/designs. I want it to be very simple, and very straightforward. The main focus of the project is it's content. So the design should be very nice, but also should point to the content, not take away from it, or create distraction. People should be more focused on the words than the imagery.

I enjoy modern designs, I need a sharp aesthetic that is clean and neat. Nothing over the top.
I have attached a word document with the content I would like on the pages.

Colors
0592cd
0255a3
33a6d7
85cae6
85acd3
3276b5
9bcb3b
f04a50
f68d4c

Requirements
Should not have
• Super feminine colors/aesthetics

```html
<!DOCTYPE html>
<html lang="en">
<head>
<meta charset="utf-8">
<title>Lantern Over Fields – Gospel Booklet Spreads</title>
<link rel="stylesheet" href="https://fonts.googleapis.com/css2?family=Archivo+Black&family=Bebas+Neue&display=swap">
<style>
  :root {
    --paper: #ffffff;
    --frame: #2b2b2b;
    --rule: #c9c9c9;
    --navy: #1c5594;
    --rust: #8a462a;
    --ink-light: #ffffff;
  }
  * { margin: 0; padding: 0; box-sizing: border-box; }
  html, body { width: 1200px; height: 1200px; overflow: hidden; background: var(--paper); }
  .canvas {
    position: relative; width: 1200px; height: 1200px;
    border: 2px solid var(--frame); background: var(--paper);
  }
  .spread { position: absolute; left: 25px; width: 1149px; height: 574px; }
  .spread--christ { top: 18px; }
  .spread--response { top: 608px; }
  .page { position: absolute; top: 0; height: 574px; }
  .page--left { left: 0; width: 575px; background: var(--paper); border: 1px solid var(--rule); }
  .page--right { left: 575px; width: 574px; }
  .spread--christ .page--right { background: var(--navy); }
  .spread--response .page--right { background: var(--rust); }

  .title-word {
    position: absolute; font-family: "Archivo Black", sans-serif;
    line-height: 1; white-space: nowrap;
    -webkit-background-clip: text; background-clip: text; color: transparent;
    transform-origin: top left;
  }
  .title-word--christ {
    left: 91px; top: 240px; font-size: 98px; letter-spacing: -4px;
    transform: scaleY(1.02);
    background-image: linear-gradient(90deg, #2a1a10 0%, #5a3a22 20%, #8a6a4a 40%, #6b4a2a 55%, #3a4a6a 68%, #1a1410 80%, #000 100%);
  }
  .title-word--response {
    left: 13px; top: 240px; font-size: 96px; letter-spacing: -5px;
    transform: scaleY(1.05);
    background-image: linear-gradient(90deg, #6b5a45 0%, #8a6a4e 18%, #5a3a26 38%, #b07a4a 50%, #d8b07a 65%, #e8c890 80%, #c9a07a 100%);
  }

  .highlight-band { position: absolute; background: var(--paper); z-index: 0; }
  .band--love-a { left: 113px; top: 220px; width: 461px; height: 32px; }
  .band--love-b { left: 0; top: 252px; width: 468px; height: 33px; }
  .band--pray { left: 0; top: 352px; width: 414px; height: 30px; }

  .line {
    position: absolute; z-index: 1; white-space: nowrap;
    font-family: "Bebas Neue", sans-serif; font-size: 32px; line-height: 32px;
    color: var(--ink-light);
  }
  .spread--christ .line { left: 126px; }
  .spread--response .line { left: 80px; }
  .line--on-navy { color: var(--navy); }

  .line--call {
    font-family: "Archivo Black", sans-serif; font-size: 27px; line-height: 31px;
    letter-spacing: 0.3px; text-transform: uppercase;
  }
  .line--on-rust { color: var(--rust); }
</style>
</head>
<body>
<main class="canvas">
  <section class="spread spread--christ">
    <div class="page page--left">
      <span class="title-word title-word--christ" role="img" aria-label="The word CHRIST filled with a stained-glass church window image">CHRIST</span>
    </div>
    <div class="page page--right">
      <div class="highlight-band band--love-a"></div>
      <div class="highlight-band band--love-b"></div>
      <p class="line" style="top:125px">BUT THAT IS NOT WHAT</p>
      <p class="line" style="top:157px">GOD WANTS.</p>
      <p class="line line--on-navy" style="top:222px">GOD LOVES YOU SO MUCH HE</p>
      <p class="line line--on-navy" style="top:254px">GAVE UP HIS ONLY SON TO SAVE YOU.</p>
      <p class="line" style="top:320px">JESUS CHRIST DIED</p>
      <p class="line" style="top:352px">ON THE CROSS IN OUR PLACE</p>
      <p class="line" style="top:385px">TO PAY FOR OUR SIN AND ROSE</p>
      <p class="line" style="top:418px">AGAIN ON THE 3RD DAY.</p>
    </div>
  </section>

  <section class="spread spread--response">
    <div class="page page--left">
      <span class="title-word title-word--response" role="img" aria-label="The word RESPONSE filled with a warm painted image over a hazy mountain landscape">RESPONSE</span>
    </div>
    <div class="page page--right">
      <p class="line" style="top:67px">SO NOW IF ANYONE:</p>
      <p class="line" style="top:133px">1. AGREES WITH GOD THEY ARE CORRUPT.</p>
      <p class="line" style="top:165px">2. BELIEVES JESUS CHRIST WILL SAVE THEM.</p>
      <p class="line" style="top:199px">3. AND ACCEPTS HIM AS THEIR PERSONAL</p>
      <p class="line" style="top:233px">LORD AND SAVIOR, JESUS CHRIST WILL FORGIVE</p>
      <p class="line" style="top:265px">THEIR CORRUPTION, RECONCILE THEM TO GOD,</p>
      <p class="line" style="top:299px">AND COME AND LIVE INSIDE THEM.</p>
      <div class="highlight-band band--pray"></div>
      <p class="line line--call line--on-rust" style="top:352px">You can pray to</p>
      <p class="line line--call" style="top:382px">Jesus Christ right now</p>
      <p class="line line--call" style="top:413px">and ask Him to save</p>
      <p class="line line--call" style="top:444px">you using the above</p>
      <p class="line line--call" style="top:474px">three steps as your</p>
      <p class="line line--call" style="top:504px">prayer guide.</p>
    </div>
  </section>
</main>
</body>
</html>
```